Painting Contractor Business Card Design

We are looking for a cool, bold, modern, polished, business card design. We are a high-end residential painting contractor. Please incorporate our logo and keep with our green/black color scheme. We are interested in seeing 2-sided and 1-sided options. Thank you very much!

Industry/Entity Type

Business

Contact Information for Business Card

Info for the card:
Owen Talsky
mobile 206-555-0193
email owen@kestrowfinish.net
web www.kestrowfinish.net

```html
<!DOCTYPE html>
<html lang="en">
<head>
<meta charset="utf-8">
<title>Kestrow Finish – Business Card</title>
<link rel="stylesheet" href="https://fonts.googleapis.com/css2?family=Orbitron:wght@600;700&display=swap">
<style>
  :root {
    --ink: #141414;
    --slate: #8c93a3;
    --mist: #b9c6e0;
    --mint: #8fe0a8;
    --green: #3ee65a;
    --brand-green: #2bb673;
    --paper: #ffffff;
  }
  * { margin: 0; padding: 0; box-sizing: border-box; }
  html, body {
    width: 1200px;
    height: 900px;
    overflow: hidden;
    background: var(--paper);
  }
  .card {
    position: relative;
    width: 1200px;
    height: 900px;
    background: var(--paper);
    font-family: "Orbitron", "Arial", sans-serif;
    color: var(--ink);
  }
  .company-heading {
    position: absolute;
    left: 84px;
    top: 56px;
    font-size: 32px;
    font-weight: 700;
    letter-spacing: 1px;
    color: var(--ink);
  }
  .brand-mark {
    position: absolute;
    left: 380px;
    top: 145px;
    width: 440px;
    height: 335px;
    display: flex;
    align-items: center;
    justify-content: center;
    gap: 18px;
  }
  .brand-mark__square {
    width: 34px;
    height: 34px;
    background: var(--brand-green);
    flex: none;
  }
  .brand-mark__name {
    font-size: 40px;
    font-weight: 700;
    color: var(--brand-green);
    white-space: nowrap;
  }
  .contact {
    position: absolute;
    left: 64px;
    top: 528px;
    font-weight: 700;
    font-size: 35px;
    letter-spacing: 1px;
    line-height: 1;
  }
  .contact__line {
    display: block;
    width: max-content;
    background-clip: text;
    -webkit-background-clip: text;
    color: transparent;
    -webkit-text-fill-color: transparent;
  }
  .contact__title {
    margin-bottom: 76px;
    background-image: linear-gradient(90deg, var(--ink) 0%, var(--ink) 16%, var(--mist) 24%, var(--mint) 32%, var(--green) 45%, var(--green) 60%, var(--mist) 78%, var(--ink) 88%);
  }
  .contact__mobile {
    margin-bottom: 22px;
    background-image: linear-gradient(90deg, var(--ink) 0%, var(--ink) 14%, var(--slate) 20%, var(--mint) 34%, var(--green) 50%, var(--green) 62%, var(--mist) 72%, var(--slate) 84%, var(--ink) 96%);
  }
  .contact__email {
    margin-bottom: 22px;
    background-image: linear-gradient(90deg, var(--ink) 0%, var(--ink) 18%, var(--mist) 24%, var(--mint) 40%, var(--green) 56%, var(--green) 66%, var(--mist) 76%, var(--ink) 90%);
  }
  .contact__web {
    background-image: linear-gradient(90deg, var(--ink) 0%, var(--slate) 14%, var(--mist) 24%, var(--mint) 36%, var(--green) 52%, var(--green) 62%, var(--mist) 74%, var(--ink) 90%);
  }
</style>
</head>
<body>
  <main class="card">
    <h1 class="company-heading">Kestrow Finish</h1>

    <div class="brand-mark">
      <span class="brand-mark__square" aria-hidden="true"></span>
      <span class="brand-mark__name">Kestrow Finish</span>
    </div>

    <section class="contact">
      <h2 class="contact__line contact__title" style="font-size:35px;">Contact Information:</h2>
      <p class="contact__line contact__mobile">Owen Talsky mobile- 206-555-0193</p>
      <p class="contact__line contact__email">Email- owen@kestrowfinish.net</p>
      <p class="contact__line contact__web">Web- www.kestrowfinish.net</p>
    </section>
  </main>
</body>
</html>
```